Luma Harbor Vow Studio, Inc.

Luma Harbor Vow Studio Business Card design for Cardlyne. Clean, contemporary, creative, colorful (using colors provided). ONE SIDE SHOULD INCLUDE logo, www.lumaharborvowstudio.com, @sayidoatluma. OTHER SIDE SHOULD INCLUDE Delia Brennan. Owner & Officiant. Marisol Bay, Coralia. 555.014.2871. delia@lumaharborvowstudio.com. Colors are blue #58AA9E
and golden #e2bf80)

Target Market(s)

Destination Wedding Clients in the United States

Contact Information for Business Card

Delia Brennan
Owner & Officiant
Marisol Bay, Coralia
555.014.2871
delia@lumaharborvowstudio.com

Font styles to use
Sans Serif

Requirements
Must have
• Colorful (colors are blue #58AA9E
• and golden #e2bf80), clean, contemporary. ONE SIDE SHOULD INCLUDE logo, www.lumaharborvowstudio.com, @sayidoatluma. Other side should include Delia Brennan. Owner & Officiant. Marisol Bay, Coralia. 555.014.2871. delia@lumaharborvowstudio.com
Nice to have
• I would like to see a version that includes my bio photo, and one that doesn't include the bio photo

```html
<!DOCTYPE html>
<html lang="en">
<head>
<meta charset="utf-8">
<title>Luma Harbor Vow Studio — Business Card</title>
<link rel="stylesheet" href="https://fonts.googleapis.com/css2?family=Poppins:ital,wght@0,200;0,300;0,400;0,500;0,600;1,600&display=swap">
<style>
  :root {
    --teal: #58aa9e;
    --gold: #e2bf80;
    --tan-band: #d39b62;
    --paper: #d9d9d9;
    --white: #ffffff;
    --label: #2a2a2a;
  }
  * { box-sizing: border-box; margin: 0; padding: 0; }
  html, body { width: 1200px; height: 874px; overflow: hidden; }
  body {
    background: var(--paper);
    font-family: "Poppins", sans-serif;
    position: relative;
  }
  .side-label {
    position: absolute;
    font-weight: 600;
    font-style: italic;
    font-size: 19px;
    letter-spacing: 3px;
    color: var(--label);
    text-transform: uppercase;
  }
  .side-label--back { left: 70px; top: 70px; }
  .side-label--front { left: 990px; top: 418px; }

  .card {
    position: absolute;
    width: 560px;
    height: 320px;
    overflow: hidden;
    box-shadow: 0 10px 26px rgba(0,0,0,0.18);
  }

  /* Back side */
  .card--back { left: 70px; top: 108px; background: var(--gold); }
  .brand {
    position: absolute;
    left: 0; right: 0; top: 76px;
    text-align: center;
    color: var(--white);
  }
  .brand__mark {
    display: block;
    width: 14px; height: 14px;
    margin: 0 auto 12px;
    border-radius: 50%;
    background: var(--white);
  }
  .brand__name {
    display: block;
    font-weight: 300;
    font-size: 44px;
    line-height: 1.1;
    letter-spacing: 1px;
    text-transform: lowercase;
  }
  .brand__tagline {
    display: block;
    margin-top: 6px;
    font-weight: 400;
    font-size: 12px;
    letter-spacing: 4px;
    text-transform: uppercase;
  }
  .card__band {
    position: absolute;
    left: 0; right: 0; bottom: 0;
    height: 70px;
    background: var(--teal);
    display: flex;
    align-items: center;
    justify-content: center;
    gap: 22px;
    color: var(--white);
    font-size: 11.5px;
    letter-spacing: 1.4px;
    text-transform: uppercase;
  }
  .card__band-divider { width: 1px; height: 12px; background: var(--white); }

  /* Front side */
  .card--front { left: 570px; top: 458px; background: var(--teal); }
  .portrait {
    position: absolute;
    left: 0; top: 0; bottom: 0;
    width: 268px;
    background: linear-gradient(160deg, #cf9b66 0%, #c28c57 100%);
  }
  .portrait__caption {
    position: absolute;
    left: 0; right: 0; bottom: 0;
    height: 54px;
    background: var(--tan-band);
    color: var(--white);
    font-weight: 400;
    font-size: 18px;
    letter-spacing: 0.5px;
    text-transform: uppercase;
    display: flex;
    align-items: center;
    justify-content: center;
  }
  .contact {
    position: absolute;
    left: 300px; right: 20px; top: 40px; bottom: 30px;
    color: var(--white);
  }
  .contact__name {
    font-weight: 200;
    font-size: 32px;
    line-height: 1;
  }
  .contact__role {
    margin-top: 6px;
    font-weight: 500;
    font-size: 11.5px;
    letter-spacing: 0.8px;
    text-transform: uppercase;
  }
  .contact__list {
    list-style: none;
    position: absolute;
    left: 0; bottom: 0;
    font-size: 11px;
    font-weight: 300;
    line-height: 1;
  }
  .contact__item {
    display: flex;
    align-items: center;
    gap: 8px;
    margin-top: 11px;
  }
  .contact__icon { width: 11px; height: 11px; flex: none; }
</style>
</head>
<body>
  <p class="side-label side-label--back">Back side</p>
  <p class="side-label side-label--front">Front side</p>

  <section class="card card--back" aria-label="Business card back side">
    <div class="brand">
      <span class="brand__mark" aria-hidden="true"></span>
      <span class="brand__name">luma harbor</span>
      <span class="brand__tagline">Vow Studio</span>
    </div>
    <div class="card__band">
      <span>www.lumaharborvowstudio.com</span>
      <span class="card__band-divider" aria-hidden="true"></span>
      <span>@sayidoatluma</span>
    </div>
  </section>

  <section class="card card--front" aria-label="Business card front side">
    <div class="portrait" role="img" aria-label="Portrait photo of the studio owner on a warm tan backdrop">
      <div class="portrait__caption">Delia Brennan</div>
    </div>
    <div class="contact">
      <h1 class="contact__name">Delia Brennan</h1>
      <p class="contact__role">Owner &amp; Officiant</p>
      <ul class="contact__list">
        <li class="contact__item">
          <svg class="contact__icon" viewBox="0 0 12 12" aria-hidden="true"><path d="M6 1a3.5 3.5 0 0 0-3.5 3.5C2.5 7.3 6 11 6 11s3.5-3.7 3.5-6.5A3.5 3.5 0 0 0 6 1zm0 4.8a1.3 1.3 0 1 1 0-2.6 1.3 1.3 0 0 1 0 2.6z" fill="#fff"/></svg>
          Marisol Bay, Coralia
        </li>
        <li class="contact__item">
          <svg class="contact__icon" viewBox="0 0 12 12" aria-hidden="true"><path d="M3 1l2 2.4-1.1 1.3a6.5 6.5 0 0 0 3.4 3.4L8.6 7 11 9l-1.2 1.8C5.5 10.6 1.4 6.5 1.2 2.2z" fill="#fff"/></svg>
          555.014.2871
        </li>
        <li class="contact__item">
          <svg class="contact__icon" viewBox="0 0 12 12" aria-hidden="true"><rect x="1" y="2.5" width="10" height="7" fill="none" stroke="#fff" stroke-width="1.1"/><path d="M1 2.8l5 3.8 5-3.8" fill="none" stroke="#fff" stroke-width="1.1"/></svg>
          delia@lumaharborvowstudio.com
        </li>
        <li class="contact__item">
          <svg class="contact__icon" viewBox="0 0 12 12" aria-hidden="true"><circle cx="6" cy="6" r="4.8" fill="none" stroke="#fff" stroke-width="1.1"/><ellipse cx="6" cy="6" rx="2" ry="4.8" fill="none" stroke="#fff" stroke-width="1"/><path d="M1.2 6h9.6" stroke="#fff" stroke-width="1"/></svg>
          www.lumaharborvowstudio.com
        </li>
      </ul>
    </div>
  </section>
</body>
</html>
```